Business card for a shipping supplies business

Needing a business card design. Please see the logo. The logo with the white font should be used if there is a dark background.

We are looking for the following info on the card. Please see the sample info. We will need the info to be changed with a few different employee names and info but all will use the same template.

Business Name: The Crate Heron
Employee Name : Marcus Delaney
Position: Account Manager
Address: 4827 W. Ridge 418 S.
Fort Worth, TX 73948
email: Marcus@thecrateheron.example
telephone: 855-619-2740 x 207
website: www.getparcelkits.example

Target Market(s)

Businesses who ship products for online sales

Industry/Entity Type

Cardboard

Contact Information for Business Card

Name, title, address, website, logo, telephone number

Font styles to use
Sans Serif

Colors
EE7325
F08F49
F5BC92
FAE3D3
FDF4ED

Requirements
Must have
• Logo on back of card. Clean look, just logo, website address

```html
<!DOCTYPE html>
<html lang="en">
<head>
<meta charset="utf-8">
<title>The Crate Heron – Business Card</title>
<link href="https://fonts.googleapis.com/css2?family=Poppins:wght@400;500;600&family=Lexend:wght@500;600&display=swap" rel="stylesheet">
<style>
  :root{
    --page:#e6e6e7;
    --ink:#140c09;
    --panel:#050505;
    --orange:#ee7325;
    --orange-soft:#f08f49;
    --peach:#f5bc92;
    --text:#2a2a2a;
    --white:#ffffff;
  }
  *{box-sizing:border-box;margin:0;padding:0}
  html,body{width:1200px;height:2930px;overflow:hidden;background:var(--page)}
  body{position:relative;font-family:"Poppins",sans-serif}
  .card{position:absolute;left:138px;width:923px;height:614px;box-shadow:0 4px 10px rgba(0,0,0,.25);overflow:hidden}
  .card--front{top:823px;background:radial-gradient(ellipse at 50% 40%,#1d1410 0%,var(--ink) 70%)}
  .card--back{top:1492px;background:var(--white)}

  .brand{position:absolute;left:0;right:0;display:flex;align-items:center;justify-content:center;gap:16px;color:var(--white);font-family:"Lexend",sans-serif;font-weight:600}
  .brand__dot{border-radius:50%;background:var(--orange)}
  .card--front .brand{top:365px;font-size:60px}
  .card--front .brand__dot{width:34px;height:34px}

  .site-dots{position:absolute;top:520px;left:0;right:0;display:flex;justify-content:center;gap:5px}
  .site-dots span{width:5px;height:5px;border-radius:50%;background:#6a605b}
  .site-dots span:nth-child(2){background:#9a918c}
  .site{position:absolute;top:536px;left:0;right:0;text-align:center;font-family:"Poppins",sans-serif;font-weight:600;font-size:19px;letter-spacing:6px;color:var(--white)}
  .site em{font-style:normal;color:var(--orange)}

  .side-panel{position:absolute;left:0;top:0;width:390px;height:614px}
  .card--back .brand{left:0;width:362px;top:352px;font-size:34px;gap:10px}
  .card--back .brand__dot{width:20px;height:20px}

  .person{position:absolute;left:494px;top:145px}
  .person__name{font-family:"Lexend",sans-serif;font-weight:600;font-size:38px;letter-spacing:1px;line-height:1;color:var(--text);text-transform:uppercase}
  .person__name .first{color:var(--orange)}
  .person__role{font-size:23px;color:var(--text);line-height:1.2;margin-top:2px}

  .contacts{position:absolute;left:493px;top:266px;list-style:none}
  .contact{position:relative;display:flex;align-items:flex-start;gap:12px;color:var(--text);font-size:19px;line-height:1.2}
  .contact + .contact{margin-top:22px}
  .contact__icon{flex:none;width:27px;height:27px;border-radius:50%;background:var(--orange);display:flex;align-items:center;justify-content:center}
  .contact__icon svg{width:15px;height:15px}
  .contact__text{padding-top:3px}
  .contact--phone .contact__text{font-size:24px;font-weight:500;padding-top:0}
  .contact:not(:last-child)::after{content:"";position:absolute;left:13px;top:31px;height:16px;border-left:2px dotted var(--orange-soft)}
</style>
</head>
<body>

<section class="card card--front" aria-label="Card front">
  <div class="brand"><span class="brand__dot"></span><span>The Crate Heron</span></div>
  <div class="site-dots"><span></span><span></span><span></span></div>
  <p class="site">WWW.<em>GETPARCELKITS</em>.EXAMPLE</p>
</section>

<section class="card card--back" aria-label="Card back">
  <svg class="side-panel" viewBox="0 0 390 614" aria-hidden="true">
    <defs>
      <pattern id="scallop" width="24" height="30" patternUnits="userSpaceOnUse" y="4">
        <circle cx="12" cy="15" r="12" fill="#050505"/>
      </pattern>
    </defs>
    <rect x="0" y="0" width="362" height="614" fill="#050505"/>
    <rect x="350" y="0" width="24" height="614" fill="url(#scallop)"/>
  </svg>
  <div class="brand"><span class="brand__dot"></span><span>The Crate Heron</span></div>

  <div class="person">
    <h1 class="person__name"><span class="first">Marcus</span> Delaney</h1>
    <p class="person__role">Account Manager</p>
  </div>

  <ul class="contacts">
    <li class="contact contact--phone">
      <span class="contact__icon"><svg viewBox="0 0 24 24"><path fill="#fff" d="M6.6 10.8a15 15 0 0 0 6.6 6.6l2.2-2.2c.3-.3.7-.4 1-.2 1.1.4 2.3.6 3.6.6.6 0 1 .4 1 1V20c0 .6-.4 1-1 1A17 17 0 0 1 3 4c0-.6.4-1 1-1h3.5c.6 0 1 .4 1 1 0 1.3.2 2.5.6 3.6.1.3 0 .7-.2 1z"/></svg></span>
      <span class="contact__text">855-619-2740 X 207</span>
    </li>
    <li class="contact">
      <span class="contact__icon"><svg viewBox="0 0 24 24"><path fill="none" stroke="#fff" stroke-width="2.4" d="M12 21s-6-6-6-11a6 6 0 0 1 12 0c0 5-6 11-6 11z"/><circle cx="12" cy="10" r="2.2" fill="#fff"/></svg></span>
      <span class="contact__text">4827 W. Ridge 418 S.<br>Fort Worth, TX 73948</span>
    </li>
    <li class="contact">
      <span class="contact__icon"><svg viewBox="0 0 24 24"><rect x="3" y="5" width="18" height="14" rx="2" fill="#fff"/><path d="M3.5 6l8.5 7 8.5-7" fill="none" stroke="#ee7325" stroke-width="2"/></svg></span>
      <span class="contact__text">Marcus@thecrateheron.example</span>
    </li>
    <li class="contact">
      <span class="contact__icon"><svg viewBox="0 0 24 24"><g fill="none" stroke="#fff" stroke-width="2"><circle cx="12" cy="12" r="9"/><ellipse cx="12" cy="12" rx="4" ry="9"/><path d="M3 12h18M5 7h14M5 17h14"/></g></svg></span>
      <span class="contact__text">www.getparcelkits.example</span>
    </li>
  </ul>
</section>

</body>
</html>
```